Geschäftspapiere für Unternehmensberatung
Zielgruppe
Unternehmensberatung
Aufgabenstellung
Es soll eine Word-Vorlage als Geschäftsbrief sein.
Name, Adresse, Steuernummer, Bank können als Platzhalter angegeben werden
WICHTIG: es soll auch selbst geduckt werden können, ohne das das Logo verpixelt oder ähnliches

```html
<!DOCTYPE html>
<html lang="de">
<head>
<meta charset="utf-8">
<title>Quendral GmbH – Geschäftspapiere</title>
<link href="https://fonts.googleapis.com/css2?family=Montserrat:wght@300;400;500;600&family=Arimo:wght@400;700&display=swap" rel="stylesheet">
<style>
  :root{
    --green:#8dc63f;
    --dark:#535660;
    --charcoal:#3b3b3a;
    --stage:#e6e6e6;
    --paper:#ffffff;
    --ink:#6b6b6b;
    --faint:#dcdcdc;
    --shadow:2px 3px 5px rgba(0,0,0,.38);
  }
  *{box-sizing:border-box;margin:0;padding:0}
  html,body{width:1200px;height:1200px;overflow:hidden;background:#fff}
  body{position:relative;font-family:"Montserrat",sans-serif;color:var(--ink)}
  .stage{position:absolute;left:144px;top:0;width:916px;height:1200px;background:var(--stage)}
  .stage-strip{position:absolute;left:159px;top:0;width:881px;height:6px;background:var(--paper)}
  .sheet{position:absolute;background:var(--paper);box-shadow:var(--shadow);overflow:hidden}

  /* wordmark */
  .wordmark{display:inline-flex;align-items:center;gap:.35em;font-family:"Montserrat",sans-serif;font-weight:500;color:var(--green);letter-spacing:.06em;white-space:nowrap;line-height:1}
  .wordmark .dot{width:.55em;height:.55em;background:currentColor}
  .wordmark.light{color:var(--faint)}
  .wordmark.white{color:#fff}

  /* envelopes */
  .env-flap{position:absolute;left:0;top:0;width:345px;height:44px}
  .env-front .wordmark{position:absolute;left:50%;top:90px;transform:translate(-50%,-50%);font-size:18px}
  .env-back .wordmark{position:absolute;left:28px;top:54px;font-size:9px}
  .env-window{position:absolute;left:209px;top:89px;width:102px;height:48px;background:var(--faint);border-radius:5px}
  .contact-list{position:absolute;list-style:none;font-family:"Arimo",sans-serif;color:#333}
  .contact-list li{display:flex;align-items:center;gap:4px;white-space:nowrap}
  .ico{display:inline-block;width:6px;height:6px;background:var(--dark);flex:none}
  .ico.green{background:var(--green)}
  .env-back .contact-list{left:26px;top:98px;font-size:4.2px;line-height:8.7px}

  /* cards */
  .card{width:155px;height:89px}
  .card .name{position:absolute;font-family:"Arimo",sans-serif;font-weight:700;font-size:5.4px;color:#555}
  .card .role{position:absolute;font-family:"Arimo",sans-serif;font-size:3.4px;color:#777}
  .card .contact-list{font-size:2.8px;line-height:6.2px}
  .card .ico{width:4px;height:4px}
  .card-a .wordmark{position:absolute;right:14px;top:14px;font-size:6px}
  .card-a .name{left:16px;top:38px}
  .card-a .role{left:16px;top:45px}
  .card-a .rule{position:absolute;left:9px;top:59px;width:134px;height:1px;background:#777}
  .card-a .col-1{left:16px;top:65px}
  .card-a .col-2{left:84px;top:65px}
  .card-green{background:var(--green)}
  .card-dark{background:var(--charcoal)}
  .card-centre .wordmark{position:absolute;left:50%;top:50%;transform:translate(-50%,-50%);font-size:8.5px}
  .card-b .wordmark{position:absolute;left:19px;top:42px;font-size:6px}
  .card-b .divider{position:absolute;left:73px;top:24px;width:1px;height:50px;background:#666}
  .card-b .name{left:80px;top:25px}
  .card-b .role{left:80px;top:32px}
  .card-b .contact-list{left:80px;top:48px}
  .card-c .wordmark{position:absolute;right:16px;top:17px;font-size:6px}
  .card-c .name{left:14px;top:22px}
  .card-c .role{left:14px;top:29px}
  .card-c .contact-list{left:0;top:49px}
  .card-c .contact-list .ico{width:14px;height:4px}
  .card-c .band{position:absolute;left:0;bottom:0;width:155px;height:6px}

  /* folder */
  .folder-art{position:absolute;left:0;top:0;width:352px;height:501px}
  .folder .wordmark{position:absolute;left:50%;top:238px;transform:translate(-50%,-50%);font-size:17px}

  /* letter */
  .letter .wordmark{position:absolute;left:50%;top:56px;transform:translate(-50%,-50%);font-size:10px}
  .letter-contact{position:absolute;left:225px;top:96px;font-size:6.2px;line-height:10.3px;letter-spacing:.04em}
  .letter-body{position:absolute;left:41px;top:151px;width:300px;font-size:6.3px;line-height:9.2px;letter-spacing:.02em;font-weight:300;color:#666;white-space:nowrap}
  .letter-body p{margin-bottom:6.5px}
  .letter-body .salutation{margin-bottom:5px}
  .letter-body .signature{margin-top:22px}
  .letter-footer{position:absolute;top:440px;left:41px;width:290px;display:flex;font-size:5.2px;line-height:9px;letter-spacing:.03em}
  .letter-footer .col-left{width:172px;padding-right:10px;border-right:1px solid #666}
  .letter-footer .col-right{padding-left:14px}
</style>
</head>
<body>
<div class="stage"></div>
<div class="stage-strip"></div>

<!-- envelope front -->
<section class="sheet env-front" style="left:216px;top:134px;width:345px;height:166px">
  <svg class="env-flap" viewBox="0 0 345 44" aria-hidden="true">
    <polygon points="0,0 345,0 333,44 12,44" fill="var(--green)"/>
  </svg>
  <span class="wordmark light"><span class="dot"></span>QUENDRAL GMBH</span>
</section>

<!-- envelope back -->
<section class="sheet env-back" style="left:216px;top:352px;width:345px;height:166px">
  <span class="wordmark">QUENDRAL GMBH</span>
  <ul class="contact-list">
    <li><span class="ico"></span>(+49 0371 482 06 15)</li>
    <li><span class="ico"></span>(+49 0371 482 06 16)</li>
    <li><span class="ico"></span>info@quendral.ch</li>
    <li><span class="ico"></span>www.quendral-beratung.ch</li>
    <li><span class="ico"></span>Lindenweg 8, 09111 Nordheim</li>
  </ul>
  <div class="env-window"></div>
</section>

<!-- business cards -->
<section class="sheet card card-a" style="left:651px;top:138px">
  <span class="wordmark">QUENDRAL</span>
  <span class="name">DEIN NAME</span>
  <span class="role">Geschäftsführer</span>
  <div class="rule"></div>
  <ul class="contact-list col-1">
    <li><span class="ico green"></span>(+49 0371 482 06)</li>
    <li><span class="ico green"></span>info@quendral.ch</li>
  </ul>
  <ul class="contact-list col-2">
    <li><span class="ico green"></span>www.quendral.ch</li>
    <li><span class="ico green"></span>Lindenweg 8, Nordheim</li>
  </ul>
</section>
<section class="sheet card card-green card-centre" style="left:833px;top:138px">
  <span class="wordmark white">QUENDRAL GMBH</span>
</section>

<section class="sheet card card-b" style="left:651px;top:280px">
  <span class="wordmark">QUENDRAL</span>
  <div class="divider"></div>
  <span class="name">DEIN NAME</span>
  <span class="role">Geschäftsführer</span>
  <ul class="contact-list">
    <li><span class="ico green"></span>(+49 0371 482 06 15)</li>
    <li><span class="ico green"></span>info@quendral.ch</li>
    <li><span class="ico green"></span>www.quendral-beratung.ch</li>
    <li><span class="ico green"></span>Lindenweg 8, 09111 Nordheim</li>
  </ul>
</section>
<section class="sheet card card-dark card-centre" style="left:833px;top:280px">
  <span class="wordmark">QUENDRAL GMBH</span>
</section>

<section class="sheet card card-c" style="left:651px;top:415px">
  <span class="wordmark">QUENDRAL</span>
  <span class="name">DEIN NAME</span>
  <span class="role">Geschäftsführer</span>
  <ul class="contact-list">
    <li><span class="ico"></span>(+49 0371 482 06 15)</li>
    <li><span class="ico"></span>info@quendral.ch</li>
    <li><span class="ico"></span>www.quendral-beratung.ch</li>
    <li><span class="ico"></span>Lindenweg 8, 09111 Nordheim</li>
  </ul>
  <svg class="band" viewBox="0 0 155 6" aria-hidden="true">
    <polygon points="0,2 108,2 106,6 0,6" fill="var(--green)"/>
    <polygon points="111,0 155,0 155,6 107,6" fill="var(--dark)"/>
  </svg>
</section>
<section class="sheet card card-centre" style="left:833px;top:415px">
  <span class="wordmark">QUENDRAL GMBH</span>
</section>

<!-- folder -->
<section class="sheet folder" style="left:212px;top:586px;width:352px;height:501px">
  <svg class="folder-art" viewBox="0 0 352 501" aria-hidden="true">
    <polygon points="0,329 191,404 352,194 352,501 0,501" fill="var(--dark)"/>
    <rect x="0" y="484" width="352" height="17" fill="var(--green)"/>
  </svg>
  <span class="wordmark"><span class="dot"></span>QUENDRAL GMBH</span>
</section>

<!-- letterhead -->
<section class="sheet letter" style="left:640px;top:587px;width:352px;height:501px">
  <span class="wordmark">QUENDRAL GMBH</span>
  <div class="letter-contact">
    Telefon: 0371-4820 615<br>
    Mail: kontakt@quendral.de<br>
    Web: www.quendral.de
  </div>
  <div class="letter-body">
    <p class="salutation">Sehr geehrter Herr</p>
    <p>Lorem ipsum dolor sit amet, consectetur adipiscing elit, sed do eiusmod tempor<br>
    incididunt ut labore et dolore magna aliqua ad minim veniam, quis nostrud<br>
    exercitation ullamco laboris nisi ut aliquip ex ea commodo consequat<br>
    Duis aute irure dolor in reprehenderit in voluptate velit esse cillum dolore eu fugiat<br>
    nulla pariatur. Excepteur sint occaecat cupidatat non proident, sunt in culpa<br>
    qui officia deserunt mollit anim id est laborum</p>
    <p>incididunt ut labore et dolore magna aliquam ad minim veniam, quis nostrud<br>
    exercitation ullamco laboris nisi ut aliquip ex ea commodo consequat<br>
    Duis aute irure dolor in reprehenderit in voluptate velit esse cillum dolore eu fugiat<br>
    nulla pariatur. Excepteur sint occaecat cupidatat non proident, sunt in culpa<br>
    exercitation ullamco laboris nisi ut aliquip ex ea commodo consequat<br>
    Duis aute irure dolor in reprehenderit in voluptate velit esse cillum dolore eu fugiat<br>
    nulla pariatur. Excepteur sint occaecat cupidatat non proident, sunt in culpa<br>
    qui officia deserunt mollit anim id est laborum</p>
    <p>Lorem ipsum dolor sit amet, consectetur adipiscing elit, sed do eiusmod tempor<br>
    incididunt ut labore et dolore magna aliqua ad minim veniam, quis nostrud<br>
    exercitation ullamco laboris nisi ut aliquip ex ea commodo consequat<br>
    Duis aute irure dolor in reprehenderit in voluptate velit esse cillum dolore eu fugiat<br>
    nulla pariatur. Excepteur sint occaecat cupidatat non proident, sunt in culpa<br>
    qui officia deserunt mollit anim id est laborum</p>
    <p class="signature">DEIN NAME</p>
  </div>
  <footer class="letter-footer">
    <div class="col-left">
      UST-ID nach § 27a UStG: DE481926374<br>
      Handelsregister: Amtsgericht Nordheim HRB 48217<br>
      Geschäftsführung: Helene Marwitz
    </div>
    <div class="col-right">
      Stadtbank Nordheim<br>
      DE44 5120 3388 0917 2245 61<br>
      NORDDEF1XXX
    </div>
  </footer>
</section>
</body>
</html>
```